Banner required for our website Sale of Silent Domestic Rangehoods

These images around silence are very good however, even more important are the family conversations that happen within the kitchen area.
These conversations are often disrupted by the use of a noisy rangehood.
A Family photos in the kitchen with a tag line relating to regaining those precious moments would be a great concept.
Regards Neil
Just a few suggestions.
I would prefer no illistrations.
Most importantly I am still seeking a visual to highlite the silent benifit of our rangehoods.The best visual will most like win this contest. We currently use the lady with the finger held to her mouth. Any other suggestions would be greatly appreciated.
We need a banner ad for the sale of designer silent domestic rangehoods.
These rangehood are aimed at the middle to higher income buyers, they are Elegant, efficient and powerful.
We aim to offer a product that exceeds our customers expectations.
Visit our website and everything we do is self explainatory.
www.mirovale.com.au
Regards Neil
Updates
Mirovale Silent rangehoods enable the family to again enjoy conversations in the kitchen
You can have friends over, revel in each others company and enjoy a great lunch or dinner without the distraction of a rangehood that sounds like a jet engine.
They also simply work better
Our promo banners typically have 2 sizes: 500x500 pixels for our socials, and a 2570*730 pixels for our Promotions page
Target Market(s)
Renovators, second home buyers, ladies between 28 and 49 years of age
Requirements
Must have
- Appealing visuals, upmarket look and feel.
Nice to have
- Family picture with kids.
Should not have
- The words Cheap, Budget nor afforadable.

```html
<!DOCTYPE html>
<html lang="en">
<head>
<meta charset="utf-8">
<title>Mirovale – Silent Domestic Rangehoods</title>
<link rel="stylesheet" href="https://fonts.googleapis.com/css2?family=Poppins:ital,wght@0,600;1,300;1,800&display=swap">
<style>
  :root {
    --pink: #fc0b6b;
    --pink-deep: #f0086c;
    --pink-dark: #c80d52;
    --dot: #dc0a5f;
    --orange: #ff8a1f;
    --white: #ffffff;
    --black: #050003;
  }
  html, body {
    margin: 0;
    padding: 0;
    width: 1200px;
    height: 341px;
    overflow: hidden;
    background: var(--pink);
  }
  .banner {
    position: relative;
    width: 1200px;
    height: 341px;
    overflow: hidden;
    background: linear-gradient(90deg, var(--pink) 0%, var(--pink-deep) 100%);
    font-family: "Poppins", sans-serif;
  }
  .decor { position: absolute; inset: 0; }
  .headline {
    position: absolute;
    left: 61px;
    top: 100px;
    margin: 0;
    color: var(--white);
    font-weight: 800;
    font-style: italic;
    font-size: 44px;
    line-height: 52px;
    letter-spacing: 0.2px;
  }
  .headline span { display: block; }
  .family-photo {
    position: absolute;
    left: 416px;
    top: 16px;
    width: 184px;
    height: 309px;
    border-radius: 40px 40px 20px 20px;
    background: linear-gradient(180deg, #d9e6f0 0%, #a9c4dc 45%, #3c5a84 100%);
  }
  .tagline-rule {
    position: absolute;
    left: 971px;
    top: 178px;
    width: 64px;
    height: 2px;
    background: var(--pink);
  }
  .tagline {
    position: absolute;
    right: 166px;
    top: 188px;
    margin: 0;
    width: 220px;
    text-align: right;
    color: var(--white);
    font-weight: 300;
    font-style: italic;
    font-size: 13px;
    line-height: 19.3px;
  }
  .brand {
    position: absolute;
    left: 1051px;
    top: 292px;
    color: var(--white);
    font-weight: 600;
    font-size: 19px;
    letter-spacing: 0.2px;
  }
</style>
</head>
<body>
<div class="banner">
  <svg class="decor" width="1200" height="341" viewBox="0 0 1200 341" aria-hidden="true">
    <defs>
      <pattern id="dots" width="19.6" height="22.4" patternUnits="userSpaceOnUse">
        <circle cx="3.7" cy="3.7" r="3.7" fill="#dc0a5f"/>
      </pattern>
      <linearGradient id="scene" x1="0" y1="0" x2="1" y2="1">
        <stop offset="0" stop-color="#2a0014"/>
        <stop offset="0.45" stop-color="#6a0a3a"/>
        <stop offset="0.75" stop-color="#1a0010"/>
        <stop offset="1" stop-color="#050003"/>
      </linearGradient>
    </defs>
    <!-- dot grids -->
    <rect class="dot-grid" x="40.5" y="212.5" width="117.6" height="123" fill="url(#dots)"/>
    <rect class="dot-grid" x="614.5" y="110.5" width="117.6" height="123" fill="url(#dots)"/>
    <!-- pills -->
    <rect class="pill" x="109" y="72" width="103" height="26" rx="13" fill="#c80d52"/>
    <rect class="pill" x="528" y="251" width="94" height="26" rx="13" fill="#c80d52"/>
    <!-- orange circles -->
    <circle class="accent-dot" cx="95" cy="38" r="16" fill="#ff8a1f"/>
    <circle class="accent-dot" cx="375" cy="312" r="10" fill="#ff8a1f"/>
    <circle class="accent-dot" cx="509" cy="345" r="33" fill="#ff8a1f"/>
    <!-- curved product window -->
    <path class="frame-outer" d="M612,0 L1200,0 L1200,252 C1150,256 1100,284 985,284 C840,283 710,185 612,0Z" fill="#050003"/>
    <path class="frame-white" d="M626,0 L1200,0 L1200,247 C1150,251 1100,279 985,279 C845,278 720,180 626,0Z" fill="#ffffff"/>
    <path class="frame-inner" d="M648,0 L1200,0 L1200,241 C1150,245 1100,271 985,271 C852,270 735,172 648,0Z" fill="#050003"/>
    <path class="product-scene" role="img" aria-label="Stainless steel chimney rangehood above a cooktop with glowing pink light streaks"
          d="M652,0 L1200,0 L1200,239 C1150,243 1100,268 985,268 C855,267 740,170 652,0Z" fill="url(#scene)"/>
  </svg>

  <h1 class="headline"><span>Silent</span><span>Domestic</span><span>Rangehoods</span></h1>

  <div class="family-photo" role="img" aria-label="Smiling family of three – father, mother and daughter – pointing towards the rangehood"></div>

  <div class="tagline-rule"></div>
  <p class="tagline">We aim to offer a product that exceeds our customers expectations.</p>

  <div class="brand">mirovale</div>
</div>
</body>
</html>
```